Ballet Sponsorship Ad

I need to have an ad created where my commercial real estate firm has a sponsorship ad for a ballet recital. The ad should include similar company branding to other ads and include a photo of my daughter congratulating her on the recital. The ad size MUST be 8.5" wide by 5.5" tall and needs to be sent in JPG and PDF format to me.

The contact information to include in the ad is:
274 W. Tollbridge Orchard Rd
Fayetteville, NC 27415
(910) 463-5082
www.holtbankerre.com
desmond@holtbankerre.com

Real Estate

Requirements
Must have
• Photo of my daughter
• Company logo
• "Congratulations Lydia Banker"
• Company contact information

```html
<!DOCTYPE html>
<html lang="en">
<head>
<meta charset="utf-8">
<title>Recital Sponsorship Ad – Holt - Banker Real Estate</title>
<link rel="stylesheet" href="https://fonts.googleapis.com/css2?family=Questrial&display=swap">
<style>
  :root {
    --panel-grey: #e4e5e4;
    --brand-green: #1d5a36;
    --text-green: #1f6a3a;
    --white: #ffffff;
    --photo-light: #b9b9b9;
    --photo-mid: #7a7a7a;
    --photo-dark: #2e2e2e;
  }
  * { margin: 0; padding: 0; box-sizing: border-box; }
  html, body { width: 1200px; height: 776px; overflow: hidden; background: var(--panel-grey); }
  .ad {
    position: relative;
    width: 1200px;
    height: 776px;
    background: var(--panel-grey);
    font-family: "Questrial", "Century Gothic", sans-serif;
    overflow: hidden;
  }
  .recital-photo {
    position: absolute;
    left: 0; top: 0;
    width: 632px; height: 776px;
    background:
      linear-gradient(90deg, var(--photo-dark) 0%, var(--photo-mid) 12%, var(--photo-light) 40%, var(--photo-light) 70%, var(--photo-mid) 88%, var(--photo-dark) 100%),
      var(--photo-mid);
  }
  .recital-photo::after {
    content: "";
    position: absolute;
    left: 0; right: 0; bottom: 0;
    height: 190px;
    background: linear-gradient(180deg, rgba(90,90,90,0.2), rgba(60,60,60,0.8));
  }
  .greeting-band {
    position: absolute;
    left: 418px; top: 108px;
    width: 782px; height: 196px;
    background: var(--brand-green);
    color: var(--white);
  }
  .award-icon {
    position: absolute;
    left: 52px; top: 40px;
    width: 110px; height: 148px;
  }
  .greeting-lead {
    position: absolute;
    left: 250px; top: 38px;
    font-size: 42px;
    letter-spacing: 0.5px;
  }
  .greeting-name {
    position: absolute;
    left: 250px; top: 102px;
    font-size: 66px;
    letter-spacing: 0.5px;
  }
  .company-name {
    position: absolute;
    left: 668px; top: 416px;
    display: flex;
    align-items: center;
    gap: 18px;
    color: var(--brand-green);
    font-size: 40px;
    line-height: 1.1;
  }
  .company-name .mark {
    width: 70px; height: 70px;
    border-radius: 50%;
    background: var(--brand-green);
    flex: none;
  }
  .contact {
    position: absolute;
    left: 668px; top: 548px;
    list-style: none;
    color: var(--text-green);
    font-size: 24px;
    line-height: 30px;
  }
</style>
</head>
<body>
  <main class="ad">
    <div class="recital-photo" role="img" aria-label="Black-and-white photo of a young ballerina in a tutu and leg warmers, seen from behind, arms raised overhead, standing before a tall window"></div>

    <section class="greeting-band">
      <svg class="award-icon" viewBox="0 0 110 148" aria-hidden="true">
        <path d="M34 70 L14 140 L34 128 L44 146 L58 92 Z" fill="var(--white)"/>
        <path d="M76 70 L96 140 L76 128 L66 146 L52 92 Z" fill="var(--white)"/>
        <circle cx="55" cy="52" r="50" fill="var(--white)"/>
        <circle cx="55" cy="52" r="32" fill="none" stroke="var(--brand-green)" stroke-width="4"/>
      </svg>
      <p class="greeting-lead">Congratulations,</p>
      <h1 class="greeting-name">Lydia Banker</h1>
    </section>

    <div class="company-name">
      <span class="mark" aria-hidden="true"></span>
      <span>Holt - Banker<br>Real Estate, LLC</span>
    </div>

    <ul class="contact">
      <li>274 W. Tollbridge Orchard Rd</li>
      <li>Fayetteville, NC 27415</li>
      <li>(910) 463-5082</li>
      <li>www.holtbankerre.com</li>
      <li>desmond@holtbankerre.com</li>
    </ul>
  </main>
</body>
</html>
```